Neurofeedback Specialist and Sober Living Advocate and Administrator needs a logo design

I need a logo design to capture/demonstrate my work and life's mission:
I provide neurofeedback training services to people from all walks of life, especially for people in recovery from addiction and substance abuse. I am also the administrator for a beautiful sober living home on the beach in Malibu, CA .
Neurofeedback is a brain training exercise that takes advantage of the brain's ability to heal itself, and it speeds up the brain's regeneration process after it has undergone some kind of stress (such as surviving a traumatic brain injury, substance abuse, recovery from mental illness, etc.) I provide neurofeedback sessions privately and at several mental health and substance abuse recovery centers in Malibu and the surrounding areas. I also train other practitioners on how to become neurofeedback providers. I work with adults and children, all ages, with all capability levels, and with a range of needs: from Autism to Peak Performance... Neurofeedback training has been known to decrease anxiety, improve sleep, alleviate symptoms of trauma/PTSD, eliminate symptoms of depression such as fatigue, sadness, motivation issues, improve focus, it can reduce the intensity of chronic pain, help eliminate migraines and seizures, and more. I also provide Neurofeedback to maximize peak performance and am typically the go-to neuroveedback speaiclist in the Malibu, CA area for celebrities such as sports heroes, performers (acting and music), CEO's, etc. I have a new website, brainwavecoveline.com (a work in progress) which features some of the colors I like (such as blue and green) but I also like most other colors except for orange and brown colors, those shades would be the two that I would typically reject.
As the administrator for the sober living home, I help clients get and stay sober as they transition back into their lives... I help guide our clients back into "the real world" after they have completed at least 30 days of treatment at an inpatient rehab or mental health facility. Our sober living website is ClearHarborHouseAtShore.com, the colors are blue and white, and our sober living home is considered a boutique business, as we provide personal attention and care, and we can host no more than 10 clients at a time.
Maybe on one side of the card you could have the Neurofeedback Specialist info and on the other side you could have the Sober Living Advocate and Administrator info...

```html
<!DOCTYPE html>
<html lang="en">
<head>
<meta charset="utf-8">
<title>Business Cards – Brainwave Cove Line &amp; Clear Harbor House</title>
<link href="https://fonts.googleapis.com/css2?family=Open+Sans:wght@400;600;700&display=swap" rel="stylesheet">
<style>
  :root {
    --backdrop: #e9e9e7;
    --card: #ffffff;
    --ink: #4a5560;
    --teal: #7ecdc4;
    --blue: #4592cc;
    --slate: #56616b;
  }
  * { box-sizing: border-box; margin: 0; padding: 0; }
  html, body { width: 1200px; height: 1000px; overflow: hidden; }
  body {
    background: var(--backdrop);
    font-family: "Open Sans", Arial, sans-serif;
    color: var(--ink);
    position: relative;
  }
  .card {
    position: absolute;
    left: 266px;
    width: 666px;
    height: 397px;
    background: var(--card);
    overflow: hidden;
  }
  .card--neuro { top: 74px; --accent: var(--teal); }
  .card--sober { top: 533px; --accent: var(--blue); }

  .brand {
    position: absolute;
    left: 36px;
    top: 120px;
    display: flex;
    align-items: center;
    gap: 12px;
    font-size: 30px;
    font-weight: 700;
    color: var(--accent);
    letter-spacing: 0.2px;
  }
  .brand__dot {
    width: 22px; height: 22px;
    border-radius: 50%;
    background: var(--accent);
  }
  .card--sober .brand { color: var(--blue); }
  .card--sober .brand__dot { border-radius: 0; }

  .contact {
    position: absolute;
    left: 39px;
    top: 228px;
    font-size: 16px;
    line-height: 22px;
  }
  .contact__address { margin-bottom: 9px; }
  .contact__line {
    display: flex;
    align-items: center;
    gap: 7px;
    height: 21.5px;
  }
  .contact__icon { width: 14px; height: 14px; fill: var(--accent); flex: none; }

  .person {
    position: absolute;
    right: 31px;
    top: 278px;
    text-align: right;
  }
  .person__name {
    font-size: 19px;
    font-weight: 700;
    color: var(--accent);
    letter-spacing: 0.3px;
    line-height: 24px;
  }
  .person__title { font-size: 16px; line-height: 22px; }
</style>
</head>
<body>

<svg width="0" height="0" style="position:absolute" aria-hidden="true">
  <symbol id="icon-phone" viewBox="0 0 16 16"><path d="M2 5c0-2 2-3 6-3s6 1 6 3v1h-3V5H5v1H2zM4 7h8l2 6H2z"/></symbol>
  <symbol id="icon-fax" viewBox="0 0 16 16"><path d="M4 1h8v4H4zM1 6h14v6h-3v-2H4v2H1zM4 11h8v4H4z"/></symbol>
  <symbol id="icon-mail" viewBox="0 0 16 16"><path d="M1 3h14v1L8 9 1 4zM1 6l7 5 7-5v7H1z"/></symbol>
  <symbol id="icon-web" viewBox="0 0 16 16"><path d="M8 1a7 7 0 1 0 0 14A7 7 0 0 0 8 1zm0 2a5 5 0 0 1 4.9 4H9l-1 3-2-3H3.1A5 5 0 0 1 8 3z"/></symbol>
</svg>

<section class="card card--neuro">
  <div class="brand"><span class="brand__dot"></span>Brainwave Cove Line</div>
  <div class="contact">
    <p class="contact__address">418 Larkspur Ave, #120<br>Westbrook TX 75210</p>
    <p class="contact__line"><svg class="contact__icon"><use href="#icon-phone"/></svg>+ 000 000 0000</p>
    <p class="contact__line"><svg class="contact__icon"><use href="#icon-fax"/></svg>+ 000 000 0000</p>
    <p class="contact__line"><svg class="contact__icon"><use href="#icon-mail"/></svg>info@brainwavecoveline.com</p>
    <p class="contact__line"><svg class="contact__icon"><use href="#icon-web"/></svg>www.brainwavecoveline.com</p>
  </div>
  <div class="person">
    <p class="person__name">DANA WHITFIELD</p>
    <p class="person__title">Trained Specialist</p>
  </div>
</section>

<section class="card card--sober">
  <div class="brand"><span class="brand__dot"></span>Clear Harbor House</div>
  <div class="contact">
    <p class="contact__address">418 Larkspur Ave, #120<br>Westbrook TX 75210</p>
    <p class="contact__line"><svg class="contact__icon"><use href="#icon-phone"/></svg>+ 000 000 0000</p>
    <p class="contact__line"><svg class="contact__icon"><use href="#icon-fax"/></svg>+ 000 000 0000</p>
    <p class="contact__line"><svg class="contact__icon"><use href="#icon-mail"/></svg>info@brainwavecoveline.com</p>
    <p class="contact__line"><svg class="contact__icon"><use href="#icon-web"/></svg>www.brainwavecoveline.com</p>
  </div>
  <div class="person">
    <p class="person__name">DANA WHITFIELD</p>
    <p class="person__title">Trained Specialist</p>
  </div>
</section>

</body>
</html>
```